Business card design needed

Family General Practitioner/ Family Physician.
Logo is the logo of the Crestmoor Guild of Family Clinicians Australia
http://kvplm.tarevo.edu.au/PictureGallery/logos/pages/CGFC%20logo_jpg.htm

Reason: Just a bit more time to make changes and the weekend for me to look at things closely and to choose. Thanks, Lumi

Thanks for all the submissions. So many of them are really works of art. Not one of them are not good. The ones that I am eliminating are the ones that I think are not suitable for me personally only, and because if I don't, it makes it very difficult to decide as many of you are also sending me slight variations of a card. I have just decided to choose a second place card too. Can't thank you all enough. Good luck, Lumi. P.S - Working today till 10 pm as the card says :-), so probably won't be able to give a feedback till late Saturday night or Sunday morning here in Sydney, Australia. 

Reason: Just added a second place to the budget and realised that Australia is ahead of the rest of the world in the time zone (only :-) - don't want to offend anyone or start a debate!! ) , so Monday deadline will mean it will be a weekend for the rest of the world. Just wanted to give everyone more time to submit their best, especially since I will be picking a second card too. Can't thank everyone enough for the submissions. P.S - Not keen on photos on the card.

Contact Information for Business Card

Dr. Lumi Harcourt M.B.B.S., F.C.G.F.C
Family General Practitioner
Address, timings, phone and fax number on the back.

Requirements
Must have
• Timings
Mon 7 am - 7 pm
Tues 7 am - 12 pm
Wed 7 am - 10 pm
Thurs 7 am - 12 pm
Fri 7 am - 8 pm
Sat 8 am - 10 pm
Sun - Off

```html
<!DOCTYPE html>
<html lang="en">
<head>
<meta charset="utf-8">
<title>Dr. Lumi Harcourt – Family General Practitioner</title>
<link rel="stylesheet" href="https://fonts.googleapis.com/css2?family=Montserrat:ital,wght@0,300;0,400;0,600;0,700;1,300&display=swap">
<style>
  :root {
    --green: #1f6b3c;
    --white: #ffffff;
    --figure-tone: #e9f1ec;
  }
  * { margin: 0; padding: 0; box-sizing: border-box; }
  html, body { width: 972px; height: 1200px; overflow: hidden; background: var(--white); }
  .card {
    position: relative;
    width: 972px;
    height: 1200px;
    font-family: "Montserrat", Arial, sans-serif;
    background: var(--white);
  }
  .header-band {
    position: absolute; left: 0; top: 0; width: 972px; height: 598px;
    background: var(--green);
    color: var(--white);
  }
  .doctor-name {
    position: absolute; left: 12px; top: 4px;
    font-size: 80px; font-weight: 700; letter-spacing: -1px; line-height: 1.1;
  }
  .credentials {
    position: absolute; left: 14px; top: 112px;
    font-size: 33px; font-weight: 400; letter-spacing: 1px;
  }
  .family-figures {
    position: absolute; left: 532px; top: 198px;
    width: 390px; height: 322px;
  }
  .tagline {
    position: absolute; left: 8px; top: 368px;
    font-size: 36px; font-weight: 300; font-style: italic; letter-spacing: 1px;
  }
  .tagline-rule {
    position: absolute; left: 0; top: 425px; width: 548px; height: 2px;
    background: var(--white); opacity: 0.6;
  }
  .profession {
    position: absolute; right: 14px; top: 530px;
    font-size: 53px; font-weight: 600;
  }
  .hours-title {
    position: absolute; left: 0; top: 612px; width: 972px;
    text-align: center; color: var(--green);
    font-size: 40px; font-weight: 700;
  }
  .hours-table {
    position: absolute; left: 14px; top: 668px; width: 944px;
    color: var(--green); font-size: 40px; font-weight: 700;
    border-collapse: collapse;
  }
  .hours-table td { padding: 0; height: 50px; line-height: 50px; }
  .hours-table .time { text-align: right; font-weight: 600; }
  .footer-band {
    position: absolute; left: 0; top: 1060px; width: 972px; height: 140px;
    background: var(--green); color: var(--white);
  }
  .contact-numbers {
    position: absolute; left: 14px; right: 14px; top: 12px;
    display: flex; justify-content: space-between;
    font-size: 38px; font-weight: 600;
  }
  .address {
    position: absolute; left: 0; top: 62px; width: 972px;
    text-align: center; font-size: 31px; font-weight: 700; line-height: 38px;
  }
</style>
</head>
<body>
<div class="card">
  <header class="header-band">
    <h1 class="doctor-name">Dr. Lumi Harcourt</h1>
    <p class="credentials">M.B.B.S., F.C.G.F.C</p>
    <svg class="family-figures" viewBox="0 0 390 322" role="img" aria-label="Silhouette illustration of a family walking hand in hand">
      <rect x="0" y="0" width="390" height="322" rx="10" fill="var(--figure-tone)" opacity="0.9"/>
    </svg>
    <p class="tagline">CARING FOR YOUR HEALTH</p>
    <div class="tagline-rule"></div>
    <h2 class="profession">Family General Practitioner</h2>
  </header>

  <h3 class="hours-title">Working Hours</h3>
  <table class="hours-table">
    <tr><td>Monday</td><td class="time">7 AM - &nbsp;7 PM</td></tr>
    <tr><td>Tuesday</td><td class="time">7 AM - 12 PM</td></tr>
    <tr><td>Wednesday</td><td class="time">7 AM - 10 PM</td></tr>
    <tr><td>Thursday</td><td class="time">7 AM - 12 PM</td></tr>
    <tr><td>Friday</td><td class="time">7 AM - &nbsp;8 PM</td></tr>
    <tr><td>Saturday</td><td class="time">8 AM - 10 PM</td></tr>
  </table>

  <footer class="footer-band">
    <div class="contact-numbers">
      <span class="phone">P:02 5550 1400</span>
      <span class="fax">F:02 5550 1233</span>
    </div>
    <p class="address">Upper Level, Harbour Arcade, Linden Grove Shopping Centre<br>Ashvale, NSW 2999</p>
  </footer>
</div>
</body>
</html>
```